Talkbridge Allies co-marketing flier

We want a flier that our partners (IT consultants) can hand out to their clients and that we can send to local businesses on their behalf to demonstrate that they can help customers purchase a phone system that has professional features that they would expect in a phone solution that costs thousands of dollars.

We want the brochure to look very professional with excellent layout and use of space.

The Talkbridge Allies corporate colour is green and more details can be found at www.talkbridgeallies.com.au.

We have attached a draft Word document that contains most of the information we need but please present the information in the way YOU believe it should be laid out.

We are looking for a designer who understands the concept and uses their own skills to produce a work of art.

Target Market(s)

small businesses that want to save money but also want a modern phone with lots of features

Industry/Entity Type

Marketing

Requirements
Must have
• Must have an image of the main phone and a cordless handset to indicate that they don't need wires to set the system up.

Must have our logo and website address

Must have a box or some "placeholder" where our partners can stamp or insert their details.

Must have a "call to action" saying "Contact us for a quote"

```html
<!DOCTYPE html>
<html lang="en">
<head>
<meta charset="utf-8">
<title>Talkbridge Allies – Office Phone System Flier</title>
<link rel="stylesheet" href="https://fonts.googleapis.com/css2?family=Cabin:wght@400;500;600;700&display=swap">
<style>
  :root{
    --green-deep:#14883a;
    --green-mid:#3fa535;
    --green-lime:#c6dd3a;
    --green-pale:#eef5c8;
    --cream:#f8fbe9;
    --red:#a10d12;
    --ink:#222;
    --white:#fff;
    --tick-dark:#5fa52a;
    --tick-light:#b5d86a;
  }
  *{margin:0;padding:0;box-sizing:border-box}
  html,body{width:849px;height:1200px;overflow:hidden}
  body{font-family:"Cabin",sans-serif;color:var(--ink);background:var(--white)}
  .flier{
    position:relative;width:849px;height:1200px;overflow:hidden;
    background:linear-gradient(115deg,#dcebaa 0%,var(--cream) 40%,#fafcf0 70%,#f1f7d6 100%);
  }
  .top-band{
    position:absolute;left:0;top:0;width:849px;height:110px;
    background:linear-gradient(90deg,var(--green-deep) 0%,var(--green-mid) 35%,var(--green-lime) 62%,var(--green-pale) 100%);
  }
  .top-band svg{position:absolute;left:0;top:0}
  .brand{
    position:absolute;right:36px;top:50px;display:flex;align-items:center;gap:10px;
    font-weight:700;font-size:30px;color:var(--green-deep);letter-spacing:-.3px;
  }
  .brand-dot{width:18px;height:18px;border-radius:50%;background:var(--green-deep)}
  .headline{
    position:absolute;left:41px;top:126px;font-size:52px;line-height:60px;font-weight:700;color:var(--red);letter-spacing:.2px;
  }
  .subhead{
    position:absolute;left:41px;top:186px;font-size:27.5px;line-height:38px;font-weight:400;color:#2a2a2a;width:700px;
  }
  .desk-phone{
    position:absolute;left:31px;top:308px;width:323px;height:170px;border-radius:14px;
    background:linear-gradient(160deg,#4a4d52 0%,#8d9096 50%,#c9cbcf 100%);
  }
  .features{position:absolute;left:371px;top:266px}
  .features-title{font-size:21.5px;line-height:28px;font-weight:700;color:var(--red);letter-spacing:.35px}
  .features ul{list-style:none;margin-top:6px}
  .features li{display:flex;align-items:center;gap:9px;height:30.8px;font-size:16.5px;color:#1e1e1e}
  .features li small{font-size:11px;margin-left:4px}
  .features svg{flex:none}
  .globe{
    position:absolute;left:606px;top:470px;width:300px;height:300px;border-radius:50%;
    background:radial-gradient(circle at 35% 35%,#e6f6ee 0%,#6fcf9f 45%,#1b8a5a 85%);
  }
  .handsets{
    position:absolute;left:476px;top:670px;width:356px;height:348px;border-radius:18px;
    background:linear-gradient(160deg,#eef1f4 0%,#aeb4bc 55%,#3d4249 100%);
  }
  .partner-box{
    position:absolute;left:41px;top:693px;width:410px;height:322px;border:2px dashed var(--green-deep);
    border-radius:12px;background:rgba(255,255,255,.55);padding:24px 28px;
  }
  .partner-title{font-size:21.5px;font-weight:700;color:var(--red);letter-spacing:.35px}
  .partner-note{font-size:15px;color:#444;margin-top:6px}
  .partner-fields{list-style:none;margin-top:28px}
  .partner-fields li{
    font-size:15px;color:var(--green-deep);font-weight:600;border-bottom:1px solid #9cbf7a;
    height:44px;display:flex;align-items:flex-end;padding-bottom:5px;
  }
  .cta{
    position:absolute;left:38px;top:1044px;width:772px;height:75px;border-radius:9px;background:var(--red);
    display:flex;align-items:center;
  }
  .cta-tagline{padding-left:36px;font-size:31px;font-weight:700;color:var(--white)}
  .cta-contact{
    position:absolute;right:3px;top:3px;width:277px;height:69px;background:var(--white);border-radius:0 7px 7px 0;
    text-align:center;
  }
  .cta-label{font-size:21px;color:#222;padding-top:3px;line-height:24px}
  .cta-number{font-size:46px;font-weight:700;color:var(--red);line-height:40px;letter-spacing:.5px}
  .footer{
    position:absolute;left:0;top:1140px;width:849px;height:60px;background:var(--green-deep);
    display:flex;align-items:center;justify-content:space-between;padding:0 26px 0 41px;
    color:var(--white);font-size:19px;
  }
</style>
</head>
<body>
<main class="flier">
  <header class="top-band">
    <svg width="849" height="110" viewBox="0 0 849 110" aria-hidden="true">
      <polygon points="180,0 260,0 420,110 340,110" fill="#ffffff" opacity=".12"/>
      <polygon points="300,0 330,0 480,110 450,110" fill="#ffffff" opacity=".18"/>
      <polygon points="390,0 470,0 610,110 530,110" fill="#ffffff" opacity=".1"/>
    </svg>
    <div class="brand"><span class="brand-dot"></span>Talkbridge Allies</div>
  </header>

  <h1 class="headline">Looking for a new phone system?</h1>
  <p class="subhead">Our proven VoIP solution comes with all the professional features to service an office of up to 6 people</p>

  <div class="desk-phone" role="img" aria-label="Photo of a desk phone with colour display and corded handset"></div>

  <section class="features">
    <h2 class="features-title">Features include, but not limited, to:</h2>
    <ul>
      <li><svg width="20" height="20" viewBox="0 0 20 20"><circle cx="10" cy="10" r="9.5" fill="var(--tick-light)"/><circle cx="10" cy="10" r="7" fill="var(--tick-dark)"/><path d="M6 10.5l3 3 5-6" stroke="#fff" stroke-width="2.2" fill="none" stroke-linecap="round" stroke-linejoin="round"/></svg>very low line rental rates*</li>
      <li><svg width="20" height="20" viewBox="0 0 20 20"><circle cx="10" cy="10" r="9.5" fill="var(--tick-light)"/><circle cx="10" cy="10" r="7" fill="var(--tick-dark)"/><path d="M6 10.5l3 3 5-6" stroke="#fff" stroke-width="2.2" fill="none" stroke-linecap="round" stroke-linejoin="round"/></svg>10c local and national calls untimed</li>
      <li><svg width="20" height="20" viewBox="0 0 20 20"><circle cx="10" cy="10" r="9.5" fill="var(--tick-light)"/><circle cx="10" cy="10" r="7" fill="var(--tick-dark)"/><path d="M6 10.5l3 3 5-6" stroke="#fff" stroke-width="2.2" fill="none" stroke-linecap="round" stroke-linejoin="round"/></svg>voicemail-to-email</li>
      <li><svg width="20" height="20" viewBox="0 0 20 20"><circle cx="10" cy="10" r="9.5" fill="var(--tick-light)"/><circle cx="10" cy="10" r="7" fill="var(--tick-dark)"/><path d="M6 10.5l3 3 5-6" stroke="#fff" stroke-width="2.2" fill="none" stroke-linecap="round" stroke-linejoin="round"/></svg>Bluetooth-to-mobile</li>
      <li><svg width="20" height="20" viewBox="0 0 20 20"><circle cx="10" cy="10" r="9.5" fill="var(--tick-light)"/><circle cx="10" cy="10" r="7" fill="var(--tick-dark)"/><path d="M6 10.5l3 3 5-6" stroke="#fff" stroke-width="2.2" fill="none" stroke-linecap="round" stroke-linejoin="round"/></svg>direct in-dial to every extension</li>
      <li><svg width="20" height="20" viewBox="0 0 20 20"><circle cx="10" cy="10" r="9.5" fill="var(--tick-light)"/><circle cx="10" cy="10" r="7" fill="var(--tick-dark)"/><path d="M6 10.5l3 3 5-6" stroke="#fff" stroke-width="2.2" fill="none" stroke-linecap="round" stroke-linejoin="round"/></svg>number portability<small>(keep your number when you move)</small></li>
      <li><svg width="20" height="20" viewBox="0 0 20 20"><circle cx="10" cy="10" r="9.5" fill="var(--tick-light)"/><circle cx="10" cy="10" r="7" fill="var(--tick-dark)"/><path d="M6 10.5l3 3 5-6" stroke="#fff" stroke-width="2.2" fill="none" stroke-linecap="round" stroke-linejoin="round"/></svg>call records via spreadsheet</li>
      <li><svg width="20" height="20" viewBox="0 0 20 20"><circle cx="10" cy="10" r="9.5" fill="var(--tick-light)"/><circle cx="10" cy="10" r="7" fill="var(--tick-dark)"/><path d="M6 10.5l3 3 5-6" stroke="#fff" stroke-width="2.2" fill="none" stroke-linecap="round" stroke-linejoin="round"/></svg>flat rate local and national calls</li>
    </ul>
  </section>

  <div class="globe" role="img" aria-label="Illustration of a glossy green globe"></div>
  <div class="handsets" role="img" aria-label="Photo of six cordless handsets in chargers linked by arrows"></div>

  <section class="partner-box" aria-label="Partner details">
    <h2 class="partner-title">Your local IT partner</h2>
    <p class="partner-note">Stamp or insert your business details here</p>
    <ul class="partner-fields">
      <li>Name</li>
      <li>Company</li>
      <li>Phone</li>
      <li>Email</li>
    </ul>
  </section>

  <section class="cta">
    <p class="cta-tagline">It’s cheaper than you think</p>
    <div class="cta-contact">
      <p class="cta-label">Contact us for a Quote</p>
      <p class="cta-number">9460 2500</p>
    </div>
  </section>

  <footer class="footer">
    <span>Corvana (456 Holdings Pty Ltd)</span>
    <span>ABN: 52 631 904 278</span>
    <span>www.talkbridgeallies.com.au</span>
  </footer>
</main>
</body>
</html>
```